Wine Label for new family wine label

we need a new wine label and name for our new group winemaking project. There are 10 of us in the group, plus two wine growers and two winemakers. We will be making wines on an ongoing basis but relatively small scale. The wines will be coming from the barossa valley and coonawarra. They will be high end wines - built on great dirt, some great history with the growers, and ultimately great grapes. We will be initially producing 4 wines, a shiraz, a cab, and a blend plus one high end single block shiraz based wine.

We are looking for the wine label to reflect quality, family and friendship.

```html
<!DOCTYPE html>
<html lang="en">
<head>
<meta charset="utf-8">
<title>Tellova Shiraz – Wine Label</title>
<link rel="stylesheet" href="https://fonts.googleapis.com/css2?family=Lato:ital,wght@0,300;0,400;1,300&display=swap">
<style>
  :root {
    --backdrop: #f2f0f2;
    --label-paper: #ffffff;
    --plum: #7a2c7e;
    --ink: #3b3a3c;
    --ink-soft: #6b6a6d;
    --rule: #4a4a4c;
  }
  * { margin: 0; padding: 0; box-sizing: border-box; }
  html, body {
    width: 803px;
    height: 1200px;
    overflow: hidden;
    background: var(--backdrop);
  }
  .canvas {
    position: relative;
    width: 803px;
    height: 1200px;
    font-family: "Lato", sans-serif;
    color: var(--ink);
  }
  .label-shape {
    position: absolute;
    inset: 0;
  }
  .label-shape .paper { fill: var(--label-paper); }

  .brand {
    position: absolute;
    top: 455px;
    left: 0;
    width: 803px;
    display: flex;
    justify-content: center;
    align-items: center;
    gap: 22px;
  }
  .brand-dot {
    width: 38px;
    height: 38px;
    border-radius: 50%;
    background: var(--plum);
  }
  .brand-name {
    font-weight: 400;
    font-size: 104px;
    line-height: 1;
    letter-spacing: 2px;
    color: var(--plum);
  }

  .regions {
    position: absolute;
    top: 590px;
    left: 0;
    width: 803px;
    display: flex;
    justify-content: center;
    font-style: italic;
    font-weight: 300;
    font-size: 28px;
    color: var(--ink);
  }
  .region { width: 260px; }
  .region-west { text-align: right; padding-right: 14px; }
  .region-south { text-align: left; padding-left: 14px; }

  .centre-rule {
    position: absolute;
    left: 401px;
    top: 575px;
    width: 1.5px;
    height: 230px;
    background: var(--rule);
  }

  .varietal {
    position: absolute;
    top: 775px;
    left: 0;
    width: 803px;
    text-align: center;
    font-weight: 300;
    font-size: 96px;
    letter-spacing: 4px;
    line-height: 1;
    color: var(--ink);
  }
  .vintage, .volume {
    position: absolute;
    left: 0;
    width: 803px;
    text-align: center;
    font-weight: 300;
    font-size: 24px;
    color: var(--ink-soft);
  }
  .vintage { top: 890px; }
  .volume { top: 932px; }
</style>
</head>
<body>
  <main class="canvas">
    <svg class="label-shape" width="803" height="1200" viewBox="0 0 803 1200" aria-hidden="true">
      <circle class="paper" cx="401.5" cy="320" r="205"/>
      <rect class="paper" x="60" y="300" width="683" height="780"/>
    </svg>

    <div class="brand">
      <span class="brand-dot"></span>
      <span class="brand-name">Tellova</span>
    </div>

    <div class="centre-rule"></div>

    <div class="regions">
      <span class="region region-west">Barossa valley</span>
      <span class="region region-south">Coonawarra</span>
    </div>

    <h1 class="varietal">Shiraz</h1>
    <p class="vintage">2014</p>
    <p class="volume">750 ml</p>
  </main>
</body>
</html>
```